Asphalt Paving Specialists Business Cards

Our company is KORVEN ASPHALT. We need a business cards two of our asphalt paving team members. We're asphalt specialists.
I need two made up please. The details on the front of the each business card i would like please is as follows.
Address is 87 Tindale Ave, Clontarf, QLD, 4019.

Company Director
Gregory Pellinham
greg@korven-example.com.au
04 87 659 042
www.korven-example.com.au

Supervisor
Lewis Marchetti
lewis@korven-example.com.au
0468 701 385
www.korven-example.com.au

We do all aspects of Asphalt Paving. Specific Services include - Driveways, Carparks & sub-divisions. All Roads. Repairs and Maintenance.

We provide free quotes!

I dont have a certain way i want them to look so im open to all designs :)

** I have uploaded our logo for the KORVEN ASPHALT. HOWEVER, CAN YOU PLEASE GET RID OF THE ( PTY LTD )

Thank you
Carina Holt
KORVEN ASPHALT

Target Market(s)

Home owners and Business Owners

Contact Information for Business Card

Asphalt Paving Specialists. All aspects of Asphalt. Residential, Commercial & Industrial. Based in Brisbane.

Font styles to use
Sans Serif

Colors

Designer to choose colors to be used in the design.

Requirements
Nice to have
• maybe an image of a driveway? or Asphalt?

```html
<!DOCTYPE html>
<html lang="en">
<head>
<meta charset="utf-8">
<title>Korven Asphalt Business Cards</title>
<link href="https://fonts.googleapis.com/css2?family=Open+Sans:wght@400;600;700;800&display=swap" rel="stylesheet">
<style>
  :root {
    --brand-blue: #1e96d6;
    --ink: #1f1f1f;
    --paper: #ffffff;
    --stage: #e6e7e9;
    --asphalt-dark: #3b4452;
    --asphalt-mid: #5c6878;
    --asphalt-light: #8b97a6;
    --grass: #6f9a4c;
  }
  * { box-sizing: border-box; margin: 0; padding: 0; }
  html, body {
    width: 1200px; height: 1021px; overflow: hidden;
    background: var(--stage);
    font-family: "Open Sans", Arial, sans-serif;
  }
  .stage {
    position: relative; width: 1200px; height: 1021px;
    display: flex; flex-direction: column; align-items: center;
    justify-content: center; gap: 37px;
  }
  .card {
    position: relative; width: 740px; height: 452px; overflow: hidden;
    box-shadow: 0 6px 18px rgba(0,0,0,0.18);
  }

  /* Back card */
  .card-back { background: var(--asphalt-dark); }
  .driveway-photo {
    position: absolute; inset: 0;
    background:
      linear-gradient(200deg, var(--grass) 0%, var(--grass) 8%, transparent 16%),
      linear-gradient(105deg, var(--asphalt-light) 0%, var(--asphalt-mid) 38%, var(--asphalt-dark) 62%, #2c333d 100%);
  }
  .back-brand {
    position: absolute; top: 150px; left: 0; right: 0;
    display: flex; align-items: center; justify-content: center; gap: 16px;
  }
  .brand-dot { width: 22px; height: 22px; border-radius: 50%; background: var(--brand-blue); }
  .brand-name {
    font-weight: 800; font-size: 54px; letter-spacing: 3px; line-height: 1;
  }
  .back-brand .brand-name { color: #ffffff; }
  .services {
    position: absolute; top: 296px; left: 40px; right: 40px;
    color: #ffffff; text-align: center; font-size: 17px; line-height: 1.4;
  }
  .quote-band {
    position: absolute; top: 360px; left: 0; right: 0; height: 40px;
    background: var(--brand-blue);
    display: flex; align-items: center; justify-content: center;
  }
  .quote-band span {
    color: #0e2a44; font-weight: 700; font-size: 18px; letter-spacing: 0.5px;
  }

  /* Front card */
  .card-front { background: var(--paper); }
  .front-brand {
    position: absolute; top: 100px; left: 0; right: 0;
    display: flex; align-items: center; justify-content: center; gap: 16px;
  }
  .front-brand .brand-name { color: var(--brand-blue); }
  .person {
    position: absolute; top: 250px; left: 120px; width: 250px; text-align: right;
  }
  .person-name { color: var(--brand-blue); font-weight: 700; font-size: 25px; }
  .person-role { color: var(--ink); font-size: 18px; margin-top: 2px; }
  .divider {
    position: absolute; top: 250px; left: 395px; width: 1px; height: 80px;
    background: #9a9a9a;
  }
  .contacts {
    position: absolute; top: 252px; left: 420px; list-style: none;
  }
  .contacts li {
    display: flex; align-items: center; gap: 10px;
    color: var(--ink); font-size: 18px; line-height: 27px;
  }
  .contacts svg { width: 16px; height: 16px; flex: none; }
  .address {
    position: absolute; top: 362px; left: 0; right: 0; text-align: center;
    color: var(--ink); font-size: 19px;
  }
</style>
</head>
<body>
<main class="stage">
  <section class="card card-back">
    <div class="driveway-photo" role="img" aria-label="Photograph of a freshly paved asphalt driveway beside a stone path and grass verge"></div>
    <div class="back-brand">
      <span class="brand-dot"></span>
      <span class="brand-name">KORVEN ASPHALT</span>
    </div>
    <p class="services">We do all aspects of Asphalt Paving. Specific Services include<br>Driveways, Carparks &amp; sub-divisions. All Roads. Repairs and Maintenance.</p>
    <div class="quote-band"><span>WE PROVIDE FREE QUOTES!</span></div>
  </section>

  <section class="card card-front">
    <div class="front-brand">
      <span class="brand-dot"></span>
      <span class="brand-name">KORVEN ASPHALT</span>
    </div>
    <div class="person">
      <div class="person-name">Gregory Pellinham</div>
      <div class="person-role">Company Director</div>
    </div>
    <div class="divider"></div>
    <ul class="contacts">
      <li>
        <svg viewBox="0 0 16 16"><path fill="#1e96d6" d="M3.6 1.2l2.2 2.7-1.3 1.6c.9 2 2.6 3.7 4.6 4.6l1.6-1.3 2.7 2.2-1.4 2.4C7 13.2 2.8 9 2.5 3z"/></svg>
        04 87 659 042
      </li>
      <li>
        <svg viewBox="0 0 16 16"><rect x="1.5" y="3.5" width="13" height="9" fill="none" stroke="#1e96d6" stroke-width="1.5"/><path d="M1.5 3.5l6.5 5 6.5-5" fill="none" stroke="#1e96d6" stroke-width="1.5"/></svg>
        greg@korven-example.com.au
      </li>
      <li>
        <svg viewBox="0 0 16 16"><g fill="none" stroke="#1e96d6" stroke-width="1.3"><circle cx="8" cy="8" r="6.3"/><ellipse cx="8" cy="8" rx="2.8" ry="6.3"/><path d="M1.7 8h12.6M2.8 4.8h10.4M2.8 11.2h10.4"/></g></svg>
        www.korven-example.com.au
      </li>
    </ul>
    <p class="address">87 Tindale Ave, Clontarf, QLD, 4019</p>
  </section>
</main>
</body>
</html>
```